Website for virtual assistant and proofreader

Professional, feminine (but not flowery!) website offering and explaining my services as a VA and Proofreader. Probably only 7 pages: home, about, services (x2), fees, testimonials and contact page. <br/><br/>I already have most of the content, which I have uploaded so you can get an idea of waht I do. I have brand colours and logo already also uploaded. I really just need the bones of the site to be designed and am happy/capable of setting this up as a Wordpress site. I'm just rubbish at design!

Industry/Entity Type

Business Service

Coding

Coded - Design and coding required

Number of Pages Required

4 page

Other font styles liked:
• Roboto Bold + Great Vibes

Colors
3276b5
fee3d4

Requirements
Must have
• should be informative, professional, feminine. Clean, clear, CTA's links to services and fees pages
• Also, see all 3 colour codes on the attached doc.
Nice to have
• business images but place holders will do
Should not have
• Nothing flowery or cartoons! Not 'busy'

```html
<!DOCTYPE html>
<html lang="en">
<head>
<meta charset="utf-8">
<title>Maren L Hollis – Virtual Assistant and Proofreader</title>
<link href="https://fonts.googleapis.com/css2?family=Mulish:wght@300;400;600;700&display=swap" rel="stylesheet">
<style>
:root{
  --blue:#1c5080;
  --blue-dark:#174670;
  --taupe:#7b6e6c;
  --taupe-dark:#6d615f;
  --ink:#333333;
  --muted:#555555;
  --light:#f1f1f1;
  --panel:#e6e6e6;
  --white:#ffffff;
  --footer:#111111;
}
*{margin:0;padding:0;box-sizing:border-box}
html,body{width:1200px;height:4812px;overflow:hidden}
body{position:relative;font-family:'Mulish',Arial,sans-serif;color:var(--ink);background:var(--white)}
.abs{position:absolute}
.btn{position:absolute;display:flex;align-items:center;justify-content:center;color:var(--white);font-size:15px;background:var(--taupe);border-radius:2px}
.btn.blue{background:var(--blue)}

/* header */
.site-header{left:0;top:0;width:1200px;height:140px;background:var(--white)}
.brand{left:146px;top:40px;display:flex;align-items:center;gap:12px}
.brand-dot{width:34px;height:34px;border-radius:50%;background:var(--blue)}
.brand-name{font-size:24px;font-weight:600;color:var(--blue);line-height:1.1}
.brand-tag{display:block;font-size:11px;font-weight:600;color:var(--blue)}
.header-email{right:144px;top:26px;font-size:24px;font-weight:600;color:#7a7a7a;display:flex;align-items:center;gap:10px}
.main-nav{top:82px;left:0;font-size:15px;color:#666}
.main-nav span{position:absolute;white-space:nowrap}
.main-nav .active{color:var(--blue)}

/* hero */
.hero{left:0;top:140px;width:1200px;height:552px}
.hero-photo{position:absolute;inset:0;background:linear-gradient(100deg,#5b4a3f 0%,#8d7a6c 30%,#c9bfb6 55%,#a49282 80%,#6f6253 100%)}
.hero-title{right:144px;top:290px;font-size:58px;font-weight:600;color:var(--white);text-shadow:0 2px 6px rgba(0,0,0,.35)}
.hero-sub{right:144px;top:368px;font-size:15px;color:var(--white)}
.arrow{width:30px;height:30px;border-radius:50%;display:flex;align-items:center;justify-content:center}

/* intro */
.intro-title{left:142px;top:760px;font-size:56px;font-weight:600;color:var(--blue)}
.intro-copy{left:144px;top:836px;width:516px;font-size:15.5px;line-height:32px;color:var(--muted)}
.intro-frame{left:700px;top:766px;width:362px;height:449px;border:3px solid #8a7e7c}
.intro-photo{left:692px;top:774px;width:362px;height:441px;background:linear-gradient(160deg,#9c6c4d,#c9997a 45%,#6a4a3a);border:6px solid var(--white);outline:1px solid #ddd}

/* services */
.services{left:0;top:1293px;width:1200px;height:903px;background:linear-gradient(180deg,#8a7c79,#7b6e6c)}
.section-title-light{width:1200px;text-align:center;color:var(--white);font-size:56px;font-weight:600}
.services-intro{left:150px;top:1434px;width:906px;text-align:center;color:var(--white);font-size:15.5px;line-height:32px}
.service-card{width:217px;background:var(--white);text-align:center;padding-top:28px}
.service-card svg{display:block;margin:0 auto}
.service-card h3{font-size:19px;font-weight:400;color:var(--blue);line-height:24px;margin-top:18px}
.service-card p{font-size:11.5px;line-height:19px;color:var(--muted);margin:12px 14px 0}
.service-card .card-btn{display:inline-flex;margin-top:14px;background:var(--taupe);color:var(--white);font-size:15px;padding:10px 20px}
.services-tag{left:0;width:1200px;text-align:center;color:var(--white);font-size:32px;font-weight:300;line-height:45px}

/* why me */
.why-photo{left:144px;top:2278px;width:439px;height:284px;background:linear-gradient(120deg,#cfd6da,#e9e7e2 40%,#b7a18c 65%,#d6d9dc)}
.tab{left:144px;width:439px;height:47px;background:var(--taupe);color:var(--white);font-size:19px;display:flex;align-items:center;padding-left:23px}
.tab.active{background:var(--blue)}
.why-panel{left:615px;top:2278px;width:441px;height:284px;background:var(--panel);padding:24px 32px;font-size:15.5px;line-height:32px;color:var(--muted)}
.why-mark{left:660px;top:2640px;display:flex;align-items:center;gap:16px;opacity:.18}
.why-mark .brand-name{font-size:40px;color:#777}
.why-mark .brand-dot{width:60px;height:60px;background:#777}

/* certifications */
.certs{left:0;top:2930px;width:1200px;height:570px;background:var(--light)}
.section-title{width:1200px;text-align:center;color:var(--blue);font-size:56px;font-weight:600}
.cert{width:297px;height:79px;background:var(--white);box-shadow:0 1px 3px rgba(0,0,0,.1);display:flex;align-items:center;justify-content:center;text-align:center;font-size:15.5px;line-height:23px;color:#666;padding:0 40px}

/* testimonials */
.quote{left:146px;top:3660px;width:470px;font-size:21px;line-height:38.5px;color:var(--muted);font-weight:300}
.quote-author{left:146px;top:3950px;font-size:24px;color:var(--blue)}
.dot{width:15px;height:15px;border-radius:50%;background:#aaa;top:4008px}
.dot.on{background:#777}
.client-photo{left:640px;top:3645px;width:410px;height:410px;border-radius:50%;border:10px solid #eeeeee;background:radial-gradient(circle at 45% 40%,#c7a089,#8e7d72 45%,#5b6d84 75%,#4a4f58)}

/* contact */
.contact{left:0;top:4140px;width:1200px;height:552px;background:linear-gradient(180deg,#877a77,#7b6e6c)}
.field{background:var(--white);font-size:11px;color:#666;padding:11px 16px}

/* footer */
.site-footer{left:0;top:4690px;width:1200px;height:122px;background:var(--footer)}
.footer-links{left:144px;top:4733px;font-size:11px;color:#aaa}
.copyright{left:144px;top:4765px;font-size:11px;color:#888}
.social{width:20px;height:20px;border-radius:50%;border:2px solid #888;top:4733px}
</style>
</head>
<body>

<header class="abs site-header">
  <div class="abs brand">
    <span class="brand-dot"></span>
    <div class="brand-name">Maren L Hollis<span class="brand-tag">Virtual Assistant and Proofreader</span></div>
  </div>
  <div class="abs header-email">
    <svg width="24" height="18" viewBox="0 0 24 18"><rect x="0" y="0" width="24" height="18" rx="2" fill="#7a7a7a"/><path d="M1 2 L12 10 L23 2" stroke="#fff" stroke-width="2" fill="none"/></svg>
    info@marenhollis.com
  </div>
  <nav class="abs main-nav">
    <span class="active" style="left:510px">Home</span>
    <span style="left:596px">About</span>
    <span style="left:684px">Services</span>
    <span style="left:787px">Fees</span>
    <span style="left:863px">Testimonials</span>
    <span style="left:996px">Contact</span>
  </nav>
</header>

<section class="abs hero">
  <div class="hero-photo" role="img" aria-label="Photo of a woman working on a laptop at a wooden desk"></div>
</section>
<div class="abs hero-title">Allow me...</div>
<div class="abs hero-sub">to handle the details so you can get on with business.</div>
<div class="btn" style="left:824px;top:407px;width:120px;height:36px">Learn More</div>
<div class="btn blue" style="left:959px;top:407px;width:97px;height:36px">Contact</div>
<div class="abs arrow" style="left:52px;top:363px"><svg width="14" height="14" viewBox="0 0 14 14"><path d="M9 2 L4 7 L9 12" stroke="#fff" stroke-width="3" fill="none"/></svg></div>
<div class="abs arrow" style="left:1114px;top:363px;background:#3d3d3d"><svg width="14" height="14" viewBox="0 0 14 14"><path d="M5 2 L10 7 L5 12" stroke="#fff" stroke-width="3" fill="none"/></svg></div>
<svg class="abs" style="left:0;top:600px" width="1200" height="93" viewBox="0 0 1200 93">
  <polygon points="600,57 1200,16 1200,93 600,93" fill="var(--blue)"/>
  <polygon points="0,93 0,90 1200,52 1200,93" fill="#fff"/>
</svg>

<h2 class="abs intro-title">Intro</h2>
<p class="abs intro-copy">Every great leader is backed by diligent and knowledgeable support. Have you ever wondered what it would be like to have your very own personal assistant? Well, you can. A virtual assistant can do everything a full-time assistant can, with the added bonus that she can save you money. Whether you need daily help, or help with special assignments or big projects, hiring me as your VA will save you the costs typically associated with an employee–holiday pay, sick pay, overtime, taxes, and insurance, are no longer your concern. And, as a virtual assistant, I only charge for the hours I actually work–no more resource-siphoning downtime.</p>
<div class="btn" style="left:144px;top:1176px;width:120px;height:39px">Learn More</div>
<div class="abs intro-frame"></div>
<div class="abs intro-photo" role="img" aria-label="Portrait photo of the assistant smiling"></div>

<section class="abs services" role="img" aria-label="Faded office desk photo behind the services section"></section>
<h2 class="abs section-title-light" style="left:0;top:1355px">Services</h2>
<p class="abs services-intro">Do you need some Smart Office Support (SOS)? Do you have a huge project looming on the horizon? Do you just need a little support managing the growing stacks of To-Dos cluttering your desk? As a master of managing the barrage of daily details that require concise and prompt attention, SOS is my speciality, from organisation to proofreading, no detail is too small!</p>

<div class="abs service-card" style="left:144px;top:1598px;height:318px">
  <svg width="70" height="70" viewBox="0 0 70 70" fill="none" stroke="var(--blue)" stroke-width="2.5"><rect x="24" y="4" width="22" height="14"/><path d="M35 18v10M12 28h46M12 28v10M35 28v10M58 28v10"/><rect x="2" y="38" width="20" height="22"/><rect x="25" y="38" width="20" height="22"/><rect x="48" y="38" width="20" height="22"/><path d="M6 46h12M6 52h12M29 46h12M29 52h12M52 46h12M52 52h12"/></svg>
  <h3>Project<br>Management</h3>
  <p>Reliable project and team management, master of organisation</p>
  <span class="card-btn">Learn More</span>
</div>
<div class="abs service-card" style="left:376px;top:1615px;height:316px">
  <svg width="70" height="70" viewBox="0 0 70 70" fill="none" stroke="var(--blue)" stroke-width="2.5"><circle cx="35" cy="35" r="31"/><path d="M35 35V4M35 35L62 50M35 35L12 56"/><path d="M40 12l12 14M44 30l14-6M40 40l14 6" stroke-width="2"/></svg>
  <h3>Administrative and<br>Accounting Support</h3>
  <p>Work smarter not harder with the right VA by your side</p>
  <span class="card-btn">Learn More</span>
</div>
<div class="abs service-card" style="left:607px;top:1598px;height:318px">
  <svg width="70" height="70" viewBox="0 0 70 70" fill="none" stroke="var(--blue)" stroke-width="2.5"><rect x="2" y="4" width="66" height="62"/><path d="M2 16h66M8 24h26M8 30h26M40 22h22v12H40zM8 40h14v12H8zM28 40h14v12H28zM48 40h14v12H48zM8 58h54"/></svg>
  <h3>Website<br>Administration</h3>
  <p>Dependable and reliable website updates–like clockwork</p>
  <span class="card-btn">Learn More</span>
</div>
<div class="abs service-card" style="left:837px;top:1615px;height:316px">
  <svg width="90" height="70" viewBox="0 0 90 70" fill="none" stroke="var(--blue)" stroke-width="2.5"><path d="M10 6h40"/><rect x="4" y="14" width="82" height="50" rx="4"/><path d="M10 24h70M10 34h70M10 44h70M10 54h70M20 24v30M30 24v30M40 24v30M50 24v30M60 24v30M70 24v30"/></svg>
  <h3>Editorial Service/<br>Proofreading</h3>
  <p>Catching simple typos and grammatical faux pas to preserve your integrity</p>
  <span class="card-btn">Learn More</span>
</div>
<p class="abs services-tag" style="top:1975px">If you want something done right...<br>find the right person to do it!</p>
<svg class="abs" style="left:0;top:2110px" width="1200" height="87" viewBox="0 0 1200 87">
  <polygon points="0,10 600,58 0,87" fill="var(--blue)"/>
  <polygon points="0,87 1200,33 1200,87" fill="#fff"/>
</svg>

<div class="abs why-photo" role="img" aria-label="Photo of a woman on the phone at a computer in an office"></div>
<div class="abs tab active" style="top:2562px">Why Me?</div>
<svg class="abs" style="left:583px;top:2572px" width="14" height="28" viewBox="0 0 14 28"><polygon points="0,0 14,14 0,28" fill="var(--blue)"/></svg>
<div class="abs tab" style="top:2618px">Who's benefited from my help...</div>
<div class="abs tab" style="top:2674px">What I can do for you...</div>
<div class="abs tab" style="top:2730px">Sometimes your calling... well, it finds you!</div>
<div class="abs tab" style="top:2786px">Sometimes your calling... well, it finds you!</div>
<div class="abs why-panel">I offer administrative, management, and editorial services for those in need of an expert, professional, and discreet “virtual” assistant. As an independent contractor, I can offer you these services with all the same dedication and loyalty as a full-time staff assistant – at a more cost-effective rate.</div>
<div class="abs why-mark"><span class="brand-dot"></span><span class="brand-name">Maren L Hollis</span></div>

<section class="abs certs"></section>
<h2 class="abs section-title" style="left:0;top:2995px">Certification and Qualifications</h2>
<div class="abs cert" style="left:144px;top:3086px">Professional Certificate for Proofreading</div>
<div class="abs cert" style="left:450px;top:3086px">Diploma for Office Software</div>
<div class="abs cert" style="left:757px;top:3086px">Thai language – A1</div>
<div class="abs cert" style="left:144px;top:3173px">Spanish to School Level – A1</div>
<div class="abs cert" style="left:450px;top:3173px">Book-keeping Certificate Stage 1</div>
<div class="abs cert" style="left:757px;top:3173px">Qualified language teacher</div>
<div class="abs cert" style="left:144px;top:3263px">Certificate in Public House Management</div>
<div class="abs cert" style="left:450px;top:3263px">6 School Certificates and 2 Advanced Passes</div>
<div class="abs cert" style="left:757px;top:3263px">Many other online courses</div>
<svg class="abs" style="left:0;top:3415px" width="1200" height="86" viewBox="0 0 1200 86">
  <polygon points="600,40 1200,2 1200,80" fill="var(--blue)"/>
  <polygon points="0,86 0,80 1200,18 1200,86" fill="#fff"/>
</svg>

<h2 class="abs section-title" style="left:0;top:3557px">Testimonials</h2>
<p class="abs quote">“ Phasellus nisl est, condimentum vitae faucibus in, sollicitudin vel metus. Nunc sit amet consequat risus. Curabitur ac elit leo. In eleifend dui tellus, in scelerisque elit porttitor et. Integer eu massa lacinia, lacinia nulla non, volutpat purus. Sed libero felis, vestibulum dolor. ”</p>
<svg class="abs" style="left:144px;top:3908px" width="500" height="20" viewBox="0 0 500 20"><path d="M0 9H14L24 19L34 9H500" stroke="#bbb" stroke-width="1.5" fill="none"/></svg>
<div class="abs quote-author">- Dara Quill</div>
<span class="abs dot on" style="left:146px"></span>
<span class="abs dot" style="left:178px"></span>
<span class="abs dot" style="left:210px"></span>
<span class="abs dot" style="left:242px"></span>
<div class="abs client-photo" role="img" aria-label="Photo of a smiling businessman shaking hands"></div>

<section class="abs contact" role="img" aria-label="Faded office photo behind the contact form"></section>
<h2 class="abs section-title-light" style="left:0;top:4205px">Contact Us</h2>
<div class="abs field" style="left:393px;top:4286px;width:200px;height:38px">Name</div>
<div class="abs field" style="left:607px;top:4286px;width:200px;height:38px">Email</div>
<div class="abs field" style="left:393px;top:4342px;width:200px;height:38px">Phone</div>
<div class="abs field" style="left:607px;top:4342px;width:200px;height:38px">Title</div>
<div class="abs field" style="left:393px;top:4398px;width:414px;height:134px">Message</div>
<div class="btn blue" style="left:557px;top:4553px;width:88px;height:37px">Submit</div>
<svg class="abs" style="left:0;top:4620px" width="1200" height="72" viewBox="0 0 1200 72">
  <polygon points="0,14 1200,56 1200,72 0,72" fill="var(--blue)"/>
</svg>

<footer class="abs site-footer"></footer>
<div class="abs footer-links">Home &nbsp;|&nbsp; About &nbsp;|&nbsp; Services &nbsp;|&nbsp; Fees &nbsp;|&nbsp; Testimonials &nbsp;|&nbsp; Contact</div>
<div class="abs copyright">Copyright © 2020 Maren. All rights reserved.</div>
<span class="abs social" style="left:982px" aria-label="Social profile"></span>
<span class="abs social" style="left:1034px" aria-label="Social profile"></span>

</body>
</html>
```